A design led business card for the construction industry

High-end business card to match logo. White logo on dark grey/off black to the front. Matching dark font on white to back, possibly with logo design again.

We offer construction and project management services to commercial and private clients in the UK. Projetcs range from newbuilds, conversion of listed buildings and refurbishments and extensions of existing homes. Our focus is on quality and attention to detail using the highest skills.

Contact Information for Business Card

Name; Dylan Marsh BSc
Position; Project Manager
Mobile; 07961 284 657
Tel; 01632 845192
email; dylan@craftvale.co.uk
web; www.craftvale.co.uk
Address; Elmbridge Vale, KT4 7PX

Colors

Designer to choose only greyscale colors for use in the design.

Requirements
Must have
• To include the below description of the business,

CONSTRUCTION - PROJECT MANAGEMENT
Nice to have
• The posibility of the top back of the card being used as a ruler. So will have a measurement to scale in mm or an architect scale of 1:50
Should not have
• Should not be portrait

```html
<!DOCTYPE html>
<html lang="en">
<head>
<meta charset="utf-8">
<title>Craftvale — Business Card</title>
<link rel="stylesheet" href="https://fonts.googleapis.com/css2?family=Montserrat:wght@300;400&display=swap">
<style>
  :root {
    --backdrop: #141821;
    --card-light: #f7f7f6;
    --card-dark: #151a26;
    --ink-dark: #1d2230;
    --ink-dark-muted: #5a5f6b;
    --ink-light: #e9eaec;
    --ink-muted: #9ea2ab;
  }
  html, body {
    margin: 0;
    width: 1200px;
    height: 1000px;
    overflow: hidden;
    background: var(--backdrop);
    font-family: "Montserrat", sans-serif;
  }
  .canvas {
    position: relative;
    width: 1200px;
    height: 1000px;
  }
  .card {
    position: absolute;
    width: 490px;
    height: 280px;
    box-sizing: border-box;
    box-shadow: 0 30px 60px rgba(0, 0, 0, 0.45);
  }
  .card--front {
    left: 150px;
    top: 200px;
    background: var(--card-light);
    display: flex;
    flex-direction: column;
    align-items: center;
    justify-content: center;
  }
  .card--back {
    left: 560px;
    top: 520px;
    background: var(--card-dark);
    color: var(--ink-light);
    padding: 34px 36px;
  }
  .brand-square {
    display: block;
  }
  .brand-name {
    margin: 22px 0 0;
    font-weight: 400;
    font-size: 17px;
    letter-spacing: 0.42em;
    padding-left: 0.42em;
    color: var(--ink-dark);
    text-transform: uppercase;
  }
  .brand-tagline {
    margin: 10px 0 0;
    font-weight: 300;
    font-size: 8px;
    letter-spacing: 0.32em;
    padding-left: 0.32em;
    color: var(--ink-dark-muted);
    text-transform: uppercase;
  }
  .card--back .brand {
    position: absolute;
    left: 36px;
    bottom: 36px;
    display: flex;
    align-items: center;
    gap: 12px;
  }
  .card--back .brand-name {
    margin: 0;
    font-size: 12px;
    color: var(--ink-light);
  }
  .contact {
    position: absolute;
    right: 36px;
    top: 34px;
    bottom: 34px;
    text-align: right;
    display: flex;
    flex-direction: column;
    justify-content: space-between;
  }
  .person-name {
    margin: 0;
    font-weight: 400;
    font-size: 12px;
    letter-spacing: 0.14em;
    text-transform: uppercase;
  }
  .person-role {
    margin: 3px 0 0;
    font-weight: 300;
    font-size: 7px;
    letter-spacing: 0.42em;
    color: var(--ink-muted);
    text-transform: uppercase;
  }
  .contact-lines {
    margin: 0;
    font-style: normal;
    font-weight: 400;
    font-size: 12px;
    line-height: 1.45;
    letter-spacing: 0.08em;
  }
  .contact-address {
    margin: 0;
    font-weight: 400;
    font-size: 12px;
    letter-spacing: 0.08em;
  }
</style>
</head>
<body>
<main class="canvas">
  <section class="card card--front" aria-label="Card front">
    <svg class="brand-square" width="56" height="56" viewBox="0 0 56 56" aria-hidden="true">
      <rect x="2" y="2" width="52" height="52" fill="none" stroke="#1d2230" stroke-width="3"/>
    </svg>
    <h1 class="brand-name">Craftvale</h1>
    <p class="brand-tagline">Construction - Project Management</p>
  </section>

  <section class="card card--back" aria-label="Card back">
    <div class="brand">
      <svg class="brand-square" width="30" height="30" viewBox="0 0 30 30" aria-hidden="true">
        <rect x="1.5" y="1.5" width="27" height="27" fill="none" stroke="#e9eaec" stroke-width="2"/>
      </svg>
      <p class="brand-name">Craftvale</p>
    </div>
    <div class="contact">
      <div class="person">
        <p class="person-name">Dylan Marsh BSc</p>
        <p class="person-role">Project Manager</p>
      </div>
      <address class="contact-lines">
        07961 284 657<br>
        01632 845192<br>
        dylan@craftvale.co.uk<br>
        www.craftvale.co.uk
      </address>
      <p class="contact-address">Elmbridge Vale, KT4 7PX</p>
    </div>
  </section>
</main>
</body>
</html>
```